TRW General Contracting

Roofing, Siding,windows, doors, Gutter,additions, decks, garagesand hanyman services fully insured and licensed, free estimates, accept all major credit cards call (614)392-7705 email corvinwr@mailbrook.net

Target Market(s)

Home improvement

Industry/Entity Type

Home Improvement

Requirements
Must have
• Whats listed above
Nice to have
• I dont have a logo i want wording for roofing, siding, gutter, decks, additions, windows, doors, and handyman services with my phone # 614-392-7705 and email corvinwr@mailbrook.net

```html
<!DOCTYPE html>
<html lang="en">
<head>
<meta charset="utf-8">
<title>Home Improvement Services – Postcard</title>
<link href="https://fonts.googleapis.com/css2?family=Alfa+Slab+One&family=Oxygen:wght@400;700&display=swap" rel="stylesheet">
<style>
:root{
  --bg:#2b2b2d;
  --yellow:#d4cf1c;
  --red:#d21e3b;
  --ink:#262626;
  --slate:#343b47;
  --navy:#1f3c78;
  --white:#ffffff;
  --paper:#e8e8e8;
  --rule:#c9c9c9;
  --photo-sky:#8fb3d9;
  --photo-house:#8d8579;
  --photo-roof:#b5505a;
  --photo-wall:#b7a68a;
  --photo-window:#c9d2d8;
}
*{box-sizing:border-box;margin:0;padding:0}
html,body{width:1200px;height:1200px;overflow:hidden;background:var(--bg)}
body{position:relative;font-family:"Oxygen",sans-serif}
.card{position:absolute;left:200px;width:800px;background:var(--white);overflow:hidden}
.front{top:50px;height:535px}
.back{top:625px;height:525px}

/* front */
.front-header{position:absolute;left:0;top:0;width:800px;height:130px;background:var(--yellow)}
.front-header .kicker{font-family:"Alfa Slab One",serif;color:var(--red);font-size:38px;line-height:1;position:absolute;left:0;right:0;top:14px;text-align:center}
.front-header .headline{font-family:"Alfa Slab One",serif;color:var(--ink);font-size:43px;line-height:1;position:absolute;left:0;right:0;top:70px;text-align:center;letter-spacing:.5px;white-space:nowrap}
.photo{position:absolute}
.photo-main{left:2px;top:135px;width:510px;height:202px;background:linear-gradient(100deg,var(--photo-sky) 0%,#b9cde0 40%,#e0b630 62%,#5a4a3c 100%)}
.thumb{position:absolute;top:345px;width:165px;height:95px}
.thumb .img{position:absolute;left:0;top:0;width:100%;height:75px}
.thumb .label{position:absolute;left:0;bottom:0;width:100%;height:20px;background:var(--slate);color:var(--white);font-family:"Alfa Slab One",serif;font-size:12px;text-align:center;line-height:20px;letter-spacing:.5px}
.t1{left:2px}.t1 .img{background:linear-gradient(160deg,#d9d2c5,var(--photo-roof))}
.t2{left:174px}.t2 .img{background:linear-gradient(160deg,#8a8d70,var(--photo-wall))}
.t3{left:344px}.t3 .img{background:linear-gradient(160deg,var(--photo-window),#9aa3a8)}
.services{position:absolute;left:517px;top:135px;width:283px;height:205px;background:var(--slate);color:var(--white)}
.services h2{font-size:17px;font-weight:700;text-align:center;margin-top:12px}
.services ul{list-style:none;display:grid;grid-template-columns:144px 135px;row-gap:10px;padding:18px 0 0 14px}
.services li{font-size:17px;line-height:20px;display:flex;align-items:center;gap:6px;white-space:nowrap}
.services li.wide{grid-column:1/3}
.num{width:14px;height:14px;border-radius:50%;background:var(--yellow);color:var(--ink);font-size:9px;font-weight:700;display:inline-flex;align-items:center;justify-content:center;flex:none}
.credentials{position:absolute;left:517px;top:345px;width:283px;height:95px;background:var(--slate);text-align:center}
.credentials .insured{font-family:"Alfa Slab One",serif;color:var(--yellow);font-size:13px;margin-top:12px}
.credentials .divider{height:6px;background:var(--bg);opacity:.35;margin:10px 0 0}
.credentials .estimates{font-family:"Alfa Slab One",serif;color:var(--white);font-size:24px;margin-top:8px;letter-spacing:.5px}
.cards-line{position:absolute;left:0;top:440px;width:800px;height:45px;text-align:center;font-size:26px;color:var(--ink);line-height:45px;background:#f1f1f1}
.front-footer{position:absolute;left:0;top:485px;width:800px;height:50px;background:var(--slate);color:var(--white);font-size:25px;line-height:50px;padding-left:12px;white-space:nowrap}
.front-footer .sep{display:inline-block;width:1px;height:26px;background:var(--white);vertical-align:middle;margin:0 8px}
.front-footer .email{font-size:23px}

/* back */
.back-panel{position:absolute;left:0;top:0;width:385px;height:408px}
.back-title{height:48px;background:var(--yellow);font-family:"Alfa Slab One",serif;font-size:16.5px;color:var(--ink);line-height:48px;text-align:center}
.back-photo{height:220px;background:linear-gradient(180deg,var(--photo-sky) 0%,#c3d4e6 35%,var(--photo-house) 55%,#6d8a4e 90%)}
.call{height:47px;background:var(--yellow);font-family:"Alfa Slab One",serif;font-size:34px;color:var(--ink);text-align:center;line-height:50px;letter-spacing:1px}
.phone{height:55px;background:var(--slate);color:var(--white);font-size:42px;font-weight:700;text-align:center;line-height:55px}
.mail{height:38px;background:var(--navy);color:var(--white);font-size:20px;font-weight:700;text-align:center;line-height:38px}
.address-side{position:absolute;left:385px;top:0;width:415px;height:400px;background:var(--paper)}
.stamp{position:absolute;right:0;top:0;width:182px;height:162px;border-left:1px solid var(--rule);border-bottom:1px solid var(--rule)}
.rule{position:absolute;left:30px;right:0;height:1px;background:var(--rule)}
</style>
</head>
<body>

<section class="card front" aria-label="Postcard front">
  <header class="front-header">
    <div class="kicker">We Solve</div>
    <div class="headline">ALL YOUR HOUSE PROBLEMS!</div>
  </header>

  <div class="photo photo-main" role="img" aria-label="Hand holding a house key in front of a suburban home, with a contractor holding a yellow hard hat"></div>

  <div class="thumb t1"><div class="img" role="img" aria-label="Roofer working on a red roof"></div><div class="label">ROOFING</div></div>
  <div class="thumb t2"><div class="img" role="img" aria-label="Worker installing house siding"></div><div class="label">SLIDING</div></div>
  <div class="thumb t3"><div class="img" role="img" aria-label="Workers fitting a window"></div><div class="label">WINDOWS</div></div>

  <div class="services">
    <h2>We Specialize in:</h2>
    <ul>
      <li><span class="num">1</span>Roofing</li>
      <li><span class="num">6</span>Gutter</li>
      <li><span class="num">2</span>Sliding</li>
      <li><span class="num">7</span>Additions</li>
      <li><span class="num">3</span>Windows</li>
      <li><span class="num">8</span>Decks</li>
      <li><span class="num">4</span>Doors</li>
      <li><span class="num">9</span>Garages</li>
      <li class="wide"><span class="num">5</span>Handyman Services</li>
    </ul>
  </div>

  <div class="credentials">
    <div class="insured">FULLY INSURED AND LICENSED</div>
    <div class="divider"></div>
    <div class="estimates">FREE ESTIMATES</div>
  </div>

  <div class="cards-line">We accept all major credit cards</div>

  <footer class="front-footer">CALL TODAY - (614)392-7705<span class="sep"></span><span class="email">email : corvinwr@mailbrook.net</span></footer>
</section>

<section class="card back" aria-label="Postcard back">
  <div class="back-panel">
    <div class="back-title">HOME IMPROVEMENT SERVICES</div>
    <div class="back-photo" role="img" aria-label="Two-storey stone and siding house with landscaped front garden"></div>
    <div class="call">CALL TODAY</div>
    <div class="phone">614-392-7705</div>
    <div class="mail">corvinwr@mailbrook.net</div>
  </div>
  <div class="address-side">
    <div class="stamp"></div>
    <div class="rule" style="top:235px"></div>
    <div class="rule" style="top:279px"></div>
    <div class="rule" style="top:323px"></div>
    <div class="rule" style="top:367px"></div>
  </div>
</section>

</body>
</html>
```